Bilingual school website redesign

The website oruvabilingualschool.example needs a new design

It is a private school from pre kinder to third grade

They teach Spanish and English

In the same website there is a section where teachers and parents interact
Updates

Reason: We are still waiting for approval from the school's teachers.

Target Market(s)

Mostly students' parents

Industry/Entity Type

Education

Number of Pages Required

3 page

Font styles to use
Sans Serif

Requirements
Must have
• Photo gallery
• Responsive design

```html
<!DOCTYPE html>
<html lang="en">
<head>
<meta charset="utf-8">
<title>Oruva Bilingual School</title>
<link href="https://fonts.googleapis.com/css2?family=Open+Sans:wght@400;600;700&display=swap" rel="stylesheet">
<style>
:root{
  --blue:#2f4aa3;
  --blue-dark:#243b86;
  --red:#e23b3b;
  --grey-btn:#e3e3e3;
  --text:#333;
  --map:#cfd3d8;
  --white:#fff;
}
*{box-sizing:border-box;margin:0;padding:0}
html,body{width:1200px;height:2336px;overflow:hidden;background:var(--white);font-family:"Open Sans",Arial,sans-serif;color:var(--text)}
.page{position:relative;width:1200px;height:2336px}
.site-header{position:absolute;top:0;left:0;width:1200px;height:100px;background:var(--blue)}
.brand{position:absolute;left:40px;top:22px;display:flex;align-items:center;gap:12px;color:var(--white);font-weight:700;font-size:26px}
.brand-dot{width:40px;height:40px;border-radius:50%;background:var(--white)}
.lang{position:absolute;right:40px;top:10px;font-size:13px;color:var(--white)}
.nav{position:absolute;right:40px;top:58px;display:flex;gap:44px;font-size:14px;font-weight:600;color:var(--white);letter-spacing:.5px}
.hero{position:absolute;top:100px;left:0;width:1200px;height:660px;background:linear-gradient(135deg,#7c8fa6 0%,#c9b7a3 45%,#9aa8b6 100%)}
.hero-name{position:absolute;right:70px;top:250px;font-size:64px;font-weight:700;color:var(--red);text-align:right;line-height:1}
.hero-name small{display:block;font-size:26px;font-weight:700;letter-spacing:1px;margin-top:6px}
.cards{position:absolute;top:800px;left:48px;width:1104px;display:flex;gap:16px}
.card{width:264px}
.card-image{height:304px;display:flex;align-items:center;justify-content:center;text-align:center;color:var(--white);font-weight:700;font-size:30px;line-height:1.1;padding:0 14px}
.tint-red{background:linear-gradient(160deg,#f08a6e,#d9433d)}
.tint-yellow{background:linear-gradient(160deg,#f3d65a,#c9a52a)}
.tint-blue{background:linear-gradient(160deg,#6d7fd8,#3847a8)}
.tint-green{background:linear-gradient(160deg,#8fdc6a,#4aa83c)}
.read-more{margin-top:16px;height:40px;background:var(--grey-btn);font-size:13px;font-weight:600;display:flex;align-items:center;justify-content:center}
.read-more.active{background:var(--red);color:var(--white)}
.pager{position:absolute;top:1184px;right:48px;display:flex;gap:6px;align-items:center;font-size:12px}
.pager span{width:18px;height:18px;background:var(--red);color:var(--white);display:flex;align-items:center;justify-content:center}
.pager span.alt{background:var(--blue)}
.pager em{font-style:normal;color:#999}
.phone-band{position:absolute;top:1240px;left:0;width:1200px;height:140px;background:var(--blue);display:flex;align-items:center;justify-content:center;gap:26px;color:var(--white);font-size:56px;font-weight:700}
.phone-band .thin{font-weight:400}
.gallery-title{position:absolute;top:1410px;width:1200px;text-align:center;font-size:40px;font-weight:600;color:#333}
.gallery{position:absolute;top:1500px;left:48px;width:1104px;display:flex;gap:12px}
.gallery-item{width:211px;height:200px}
.g1{background:linear-gradient(160deg,#2b3f86,#6b7cb0)}
.g2{background:linear-gradient(160deg,#3a5ea8,#b68d5a)}
.g3{background:linear-gradient(160deg,#e8e4de,#9bb05e)}
.g4{background:linear-gradient(160deg,#f0ece6,#7aa7c9)}
.g5{background:#111}
.view-all{position:absolute;top:1730px;left:500px;width:200px;height:48px;background:var(--blue);color:var(--white);font-size:16px;display:flex;align-items:center;justify-content:center}
.map{position:absolute;top:1820px;left:0;width:1200px;height:260px;background:var(--map)}
.map-pin{position:absolute;top:1848px;left:580px}
.site-footer{position:absolute;top:2080px;left:0;width:1200px;height:220px;background:var(--red);color:var(--white);font-size:13px}
.foot-col{position:absolute;top:48px;line-height:1.7}
.foot-col ul{list-style:none}
.foot-col li::before{content:"› "}
.social li{display:flex;align-items:center;gap:10px;margin-bottom:8px}
.social li::before{content:none}
.social i{width:30px;height:30px;border-radius:50%;border:1px solid var(--white)}
.copyright{position:absolute;top:2300px;left:0;width:1200px;height:36px;background:var(--blue-dark);color:#cfd6ee;font-size:12px;display:flex;align-items:center;justify-content:center}
</style>
</head>
<body>
<div class="page">
  <header class="site-header">
    <div class="brand"><span class="brand-dot"></span>Oruva</div>
    <div class="lang">English | Spanish</div>
    <nav class="nav"><span>OUR SCHOOL</span><span>NEWS</span><span>ACTIVITIES</span><span>ONLINE RESOURCES</span><span>CONTACT</span></nav>
  </header>

  <section class="hero" role="img" aria-label="Classroom photo of young students raising their hands with a teacher at the board">
    <div class="hero-name">Oruva<small>BILINGUAL SCHOOL</small></div>
  </section>

  <section class="cards">
    <article class="card"><div class="card-image tint-red" role="img" aria-label="Smiling child photo">REGISTRATION PROMOTION</div><div class="read-more">READ MORE</div></article>
    <article class="card"><div class="card-image tint-yellow" role="img" aria-label="Group of students photo">PRESSTIONS EASTER</div><div class="read-more active">READ MORE</div></article>
    <article class="card"><div class="card-image tint-blue" role="img" aria-label="Students working together photo">RELEASE</div><div class="read-more">READ MORE</div></article>
    <article class="card"><div class="card-image tint-green" role="img" aria-label="Child holding books photo">CLOSED FOR VACATIONS</div><div class="read-more">READ MORE</div></article>
  </section>
  <div class="pager"><span>1</span><span class="alt">2</span><span class="alt">3</span><em>. . . .</em><span>›</span></div>

  <section class="phone-band">
    <svg width="44" height="52" viewBox="0 0 24 24" aria-hidden="true"><path fill="#fff" d="M6.6 10.8a15.1 15.1 0 0 0 6.6 6.6l2.2-2.2c.3-.3.7-.4 1-.2 1.1.4 2.3.6 3.6.6.6 0 1 .4 1 1V20c0 .6-.4 1-1 1A17 17 0 0 1 3 4c0-.6.4-1 1-1h3.5c.6 0 1 .4 1 1 0 1.3.2 2.5.6 3.6.1.3 0 .7-.2 1z"/></svg>
    <span>2240<span class="thin">-0187</span> - 2240<span class="thin">-0193</span></span>
  </section>

  <h2 class="gallery-title">PHOTO GALLERY</h2>
  <section class="gallery">
    <div class="gallery-item g1" role="img" aria-label="Students in school uniforms"></div>
    <div class="gallery-item g2" role="img" aria-label="Class activity seated on the floor"></div>
    <div class="gallery-item g3" role="img" aria-label="Student holding a folder"></div>
    <div class="gallery-item g4" role="img" aria-label="Two young students smiling"></div>
    <div class="gallery-item g5" role="img" aria-label="Video placeholder"></div>
  </section>
  <div class="view-all">VIEW ALL</div>

  <div class="map" role="img" aria-label="Street map showing the school location"></div>
  <svg class="map-pin" width="40" height="56" viewBox="0 0 24 34" aria-hidden="true"><path fill="#333" d="M12 0C5.4 0 0 5.4 0 12c0 9 12 22 12 22s12-13 12-22C24 5.4 18.6 0 12 0z"/><circle cx="12" cy="12" r="4.5" fill="#cfd3d8"/></svg>

  <footer class="site-footer">
    <div class="foot-col" style="left:48px;width:260px">
      Colonia Las Palmas, First Street,<br>Main Building, City<br><br>(504) 2240-0187, 2240-0193<br>info@oruvabilingualschool.example
    </div>
    <div class="foot-col" style="left:380px"><ul><li>FAQ</li><li>Who we are</li><li>Mission and vision</li><li>News</li><li>Events</li></ul></div>
    <div class="foot-col" style="left:640px"><ul><li>Contact Us</li><li>Requirements for Kindergarten</li><li>Requirements for Pre-kindergarten</li><li>Requirements for Primary</li><li>Terms and Conditions</li></ul></div>
    <div class="foot-col social" style="left:990px"><ul><li><i></i>Community</li><li><i></i>Updates</li><li><i></i>Network</li></ul></div>
  </footer>
  <div class="copyright">Copyright © 2015 Oruva Bilingual School. All Rights Reserved</div>
</div>
</body>
</html>
```